Prom Night 2011 theme

I am looking for a theme to best represent a high school "prom night". Design will be printed on slightly smaller than business card size paper. This is a clean sheet design, nothing is out of bounds so use you imagination. Target audience is high school age students. Design should have text "Prom Night 2011" incorporated into it. Colors are limitless.

```html
<!DOCTYPE html>
<html lang="en">
<head>
<meta charset="utf-8">
<title>Prom Night 2011</title>
<link rel="stylesheet" href="https://fonts.googleapis.com/css2?family=Advent+Pro:wght@100;200&display=swap">
<style>
  :root {
    --ink: #000000;
    --night: #02020a;
    --glow-blue: #1c1ca6;
    --deep-blue: #0a0a4a;
    --silver: #b9b9bd;
    --silver-dark: #5a5a60;
    --highlight: #ffffff;
    --title: #f4f4f4;
    --title-edge: #8a8a90;
  }
  html, body {
    margin: 0;
    padding: 0;
    overflow: hidden;
    background: var(--ink);
  }
  .card {
    position: relative;
    width: 1200px;
    height: 720px;
    background: var(--ink);
    overflow: hidden;
  }
  .halftone-field {
    position: absolute;
    left: 0;
    top: 0;
    width: 820px;
    height: 720px;
    background:
      radial-gradient(ellipse 520px 620px at 760px 40px, var(--glow-blue) 0%, var(--deep-blue) 40%, rgba(6,6,40,0.6) 65%, var(--night) 90%),
      var(--night);
  }
  .divider {
    position: absolute;
    left: 818px;
    top: 0;
    width: 20px;
    height: 720px;
  }
  .title-panel {
    position: absolute;
    left: 838px;
    top: 0;
    right: 0;
    bottom: 0;
    background: var(--ink);
  }
  .title {
    position: absolute;
    left: 842px;
    top: 48px;
    margin: 0;
    font-family: "Advent Pro", "Arial Narrow", sans-serif;
    font-weight: 100;
    font-size: 150px;
    line-height: 117px;
    letter-spacing: -4px;
    color: var(--title);
    text-shadow: 0 0 1px var(--title-edge), 0 0 2px var(--title-edge);
  }
  .title span { display: block; }
</style>
</head>
<body>
  <div class="card">
    <div class="halftone-field" role="img" aria-label="Blue glow with a black halftone dot pattern fading toward the lower left"></div>
    <svg class="divider" viewBox="0 0 20 720" aria-hidden="true">
      <defs>
        <linearGradient id="chrome" x1="0" y1="0" x2="1" y2="0">
          <stop offset="0" stop-color="var(--silver-dark)"/>
          <stop offset="0.5" stop-color="var(--silver)"/>
          <stop offset="1" stop-color="var(--silver-dark)"/>
        </linearGradient>
      </defs>
      <rect x="0" y="0" width="16" height="720" fill="url(#chrome)"/>
      <rect x="2" y="0" width="2" height="720" fill="var(--highlight)"/>
      <rect x="12" y="0" width="2" height="720" fill="var(--highlight)"/>
    </svg>
    <div class="title-panel"></div>
    <h1 class="title"><span>Prom</span><span>Night</span><span>2011</span></h1>
  </div>
</body>
</html>
```